New Company Business Card design

Looking for a corporate looking business card utilising my new logo design - the logo i would like embossed as one option and flat as another - simplistic but stylish - less is more - we are an import export business launching into the market - i would like a couple of options as main background - Grey or Black

```html
<!DOCTYPE html>
<html lang="en">
<head>
<meta charset="utf-8">
<title>Meridian Trade Partners – Business Card</title>
<link href="https://fonts.googleapis.com/css2?family=Open+Sans:wght@400;600;700&display=swap" rel="stylesheet">
<style>
  :root {
    --stage: #0096ff;
    --card-dark: #111111;
    --card-mid: #2a2a2a;
    --brand-blue: #1b7fd1;
    --brand-grey: #7a7a7a;
    --tagline-grey: #8d8d8d;
    --text-white: #ffffff;
    --text-soft: #e6e6e6;
  }
  * { margin: 0; padding: 0; box-sizing: border-box; }
  html, body {
    width: 1200px; height: 1000px; overflow: hidden;
    background: var(--stage);
    font-family: "Open Sans", Arial, sans-serif;
  }
  .stage { position: relative; width: 1200px; height: 1000px; }

  .card {
    position: absolute; top: 270px;
    width: 237px; height: 414px;
    overflow: hidden;
    background: var(--card-dark);
  }
  .card--front { left: 314px; }
  .card--back  { left: 651px; }

  .card__texture {
    position: absolute; inset: 0;
    background:
      radial-gradient(ellipse at 50% 50%, rgba(70,70,70,0.55) 0%, rgba(30,30,30,0.2) 55%, rgba(0,0,0,0) 80%),
      linear-gradient(180deg, var(--card-mid) 0%, var(--card-dark) 100%);
  }

  .brand {
    position: absolute; left: 0; right: 0;
    text-align: center;
  }
  .card--front .brand { top: 92px; }
  .card--back .brand { top: 84px; }
  .brand__name {
    display: inline-flex; align-items: center; gap: 6px;
    font-weight: 700; font-size: 13px; letter-spacing: 0.5px;
    text-transform: uppercase; line-height: 1.15;
  }
  .card--back .brand__name { font-size: 11.5px; }
  .brand__dot { width: 9px; height: 9px; border-radius: 50%; flex: none; }
  .brand__tagline {
    display: block; margin-top: 6px;
    font-size: 6px; letter-spacing: 1.6px; text-transform: uppercase;
    color: var(--tagline-grey);
  }
  .card--front .brand__name { color: var(--brand-blue); }
  .card--front .brand__dot { background: var(--brand-blue); }
  .card--back .brand__name { color: var(--brand-grey); }
  .card--back .brand__dot { background: var(--brand-grey); }

  .card__url {
    position: absolute; bottom: 17px; left: 0; right: 0;
    text-align: center; color: var(--text-white);
    font-size: 10px; font-weight: 600; letter-spacing: 1.4px;
  }

  .person { position: absolute; top: 155px; left: 23px; color: var(--text-white); }
  .person__name { font-size: 18px; font-weight: 600; line-height: 1.2; }
  .person__role { font-size: 9px; color: var(--text-soft); }
  .person__rule {
    position: absolute; top: 193px; left: 0;
    width: 181px; height: 3px; background: var(--text-white);
  }

  .contact { position: absolute; left: 22px; color: var(--text-white); font-size: 9.5px; line-height: 14px; }
  .contact__row { display: flex; align-items: center; gap: 6px; }
  .contact__icon { width: 12px; height: 12px; flex: none; }
  .contact--address { top: 286px; left: 36px; font-style: normal; }
  .contact--phone { top: 321px; }
  .contact--web { top: 356px; }
</style>
</head>
<body>
<main class="stage">

  <section class="card card--front" aria-label="Business card front">
    <div class="card__texture" role="img" aria-label="Dark charcoal mosaic of small diamond tiles"></div>
    <div class="brand">
      <span class="brand__name"><span class="brand__dot"></span>Meridian Trade Partners</span>
      <span class="brand__tagline">Worldwide supply for regional demand</span>
    </div>
    <p class="card__url">www.meridiantp.com</p>
  </section>

  <section class="card card--back" aria-label="Business card back">
    <div class="card__texture" role="img" aria-label="Dark charcoal mosaic of small diamond tiles"></div>
    <div class="brand">
      <span class="brand__name"><span class="brand__dot"></span>Meridian Trade Partners</span>
      <span class="brand__tagline">Worldwide supply for regional demand</span>
    </div>

    <div class="person">
      <h1 class="person__name">Dana Whitfield</h1>
      <p class="person__role">Business Development Manager</p>
    </div>
    <div class="person__rule"></div>

    <address class="contact contact--address">
      28/9 Harbour View Lane,<br>Eastfield QLD 4102
    </address>

    <div class="contact contact--phone contact__row">
      <svg class="contact__icon" viewBox="0 0 24 24" aria-hidden="true">
        <path d="M6.6 10.8a15 15 0 0 0 6.6 6.6l2.2-2.2c.3-.3.7-.4 1-.2 1.1.4 2.3.6 3.6.6.6 0 1 .4 1 1V20c0 .6-.4 1-1 1A17 17 0 0 1 3 4c0-.6.4-1 1-1h3.5c.6 0 1 .4 1 1 0 1.3.2 2.5.6 3.6.1.3 0 .7-.2 1z" fill="#ffffff"/>
      </svg>
      <span>+61455501234<br>+61455501234</span>
    </div>

    <div class="contact contact--web contact__row">
      <svg class="contact__icon" viewBox="0 0 24 24" aria-hidden="true" fill="none" stroke="#ffffff" stroke-width="1.6">
        <circle cx="12" cy="12" r="9.5"/>
        <ellipse cx="12" cy="12" rx="4.2" ry="9.5"/>
        <line x1="2.5" y1="12" x2="21.5" y2="12"/>
        <line x1="4" y1="7" x2="20" y2="7"/>
        <line x1="4" y1="17" x2="20" y2="17"/>
      </svg>
      <span>hello@meridiantp.com<br>www.meridiantp.com</span>
    </div>
  </section>

</main>
</body>
</html>
```